Make it POP! Label design for Australian Skin Care range

I want to see elegance, femininity, luxury, glamour.
Design needs to compliment existing logo in style and colours; turquoise and silver (see file). text required (see file)
There are 5 different products with different text - same design required.
Please see file attached for the containers the labels will be applied to.

Target Market(s)

women over 35

Industry/Entity Type

Skin Care Product

Font styles to use
Sans Serif

Colors
33b8a4

Requirements
Must have
• Design in Turquoise and silver
• Sans Serif fonts, compliment existing logo (see file)
• contain text exactly as written (see file)
Nice to have
• Feminine, flowing lines/ shapes
Should not have
• Black, nothing bold or masculine. Nothing that looks clinical or medical

```html
<!DOCTYPE html>
<html lang="en">
<head>
<meta charset="UTF-8">
<title>Cora's Bloom – Native Hydrating Serum Label</title>
<link href="https://fonts.googleapis.com/css2?family=Raleway:wght@300;400;500;600&display=swap" rel="stylesheet">
<style>
  :root {
    --turquoise: #33b8a4;
    --turquoise-deep: #2aa792;
    --turquoise-pale: #bfe8e1;
    --silver: #9a9ea1;
    --silver-light: #e3e5e6;
    --ink-grey: #8c8f92;
    --paper: #ffffff;
  }
  * { margin: 0; padding: 0; box-sizing: border-box; }
  html, body {
    width: 773px;
    height: 1200px;
    overflow: hidden;
    background: var(--paper);
  }
  .label {
    position: relative;
    width: 773px;
    height: 1200px;
    overflow: hidden;
    background: var(--paper);
    font-family: "Raleway", sans-serif;
    color: var(--ink-grey);
    text-align: center;
  }
  .flourish-silver {
    position: absolute;
    top: -40px;
    right: -60px;
    width: 380px;
    height: 380px;
    border-radius: 50%;
    background: radial-gradient(circle at 60% 40%, var(--silver-light) 0%, rgba(227,229,230,0.55) 45%, rgba(255,255,255,0) 70%);
  }
  .wave-band {
    position: absolute;
    left: 0;
    top: 0;
    width: 773px;
    height: 1200px;
  }
  .flourish-turquoise {
    position: absolute;
    left: -80px;
    top: 570px;
    width: 560px;
    height: 540px;
    border-radius: 50%;
    background: radial-gradient(ellipse at 45% 55%, rgba(191,232,225,0.9) 0%, rgba(120,206,192,0.55) 45%, rgba(51,184,164,0) 72%);
  }
  .brand-mark {
    position: absolute;
    left: 317px;
    top: 28px;
    width: 140px;
    height: 140px;
    border-radius: 50%;
    background: var(--turquoise);
    border: 6px solid var(--silver-light);
  }
  .brand-name {
    position: absolute;
    top: 190px;
    width: 100%;
    font-size: 28px;
    font-weight: 400;
    letter-spacing: 9px;
    color: var(--ink-grey);
  }
  .tagline {
    position: absolute;
    top: 236px;
    width: 100%;
    font-size: 22px;
    line-height: 28px;
    font-weight: 400;
    color: var(--turquoise);
  }
  .product-name {
    position: absolute;
    top: 364px;
    width: 100%;
    font-size: 35px;
    line-height: 46px;
    font-weight: 500;
    letter-spacing: 1px;
    color: var(--ink-grey);
  }
  .with {
    position: absolute;
    top: 478px;
    width: 100%;
    font-size: 18px;
    color: var(--ink-grey);
  }
  .ingredients {
    position: absolute;
    top: 512px;
    width: 100%;
    font-size: 24px;
    font-weight: 600;
    color: var(--turquoise);
  }
  .claim-vegan {
    position: absolute;
    left: 66px;
    top: 1020px;
    font-size: 20px;
    font-weight: 600;
    letter-spacing: 1px;
    color: var(--paper);
  }
  .claim-skin {
    position: absolute;
    left: 58px;
    top: 1060px;
    padding: 6px 18px;
    border-radius: 20px;
    background: var(--paper);
    font-size: 17px;
    font-weight: 500;
    color: var(--turquoise);
  }
  .net-weight {
    position: absolute;
    right: 52px;
    top: 1072px;
    text-align: right;
    color: var(--turquoise);
  }
  .net-weight .net-label {
    display: block;
    font-size: 18px;
    font-weight: 500;
  }
  .net-weight .net-value {
    display: block;
    font-size: 34px;
    font-weight: 600;
    line-height: 40px;
  }
</style>
</head>
<body>
<div class="label">
  <div class="flourish-silver" role="img" aria-label="Silver flowing leaf flourish ornament"></div>

  <svg class="wave-band" viewBox="0 0 773 1200" aria-hidden="true">
    <defs>
      <linearGradient id="band-fill" x1="0" y1="0" x2="1" y2="1">
        <stop offset="0" stop-color="#33b8a4"/>
        <stop offset="1" stop-color="#2aa792"/>
      </linearGradient>
    </defs>
    <path d="M0,780 C170,880 340,1000 470,1080 C560,1135 630,1170 700,1200 L0,1200 Z" fill="url(#band-fill)"/>
  </svg>

  <div class="flourish-turquoise" role="img" aria-label="Turquoise flowing leaf flourish ornament"></div>

  <div class="brand-mark" aria-hidden="true"></div>
  <div class="brand-name">CORA'S BLOOM</div>
  <div class="tagline">Natural Nourishing<br>Australian Skin Care</div>

  <h1 class="product-name">NATIVE<br>HYDRATING SERUM</h1>
  <div class="with">with</div>
  <div class="ingredients">Quandong • Lilli Pilli • Kakadu Plum</div>

  <div class="claim-vegan">100% VEGAN</div>
  <div class="claim-skin">All Skin Types</div>

  <div class="net-weight">
    <span class="net-label">Net Wt.</span>
    <span class="net-value">30ml</span>
  </div>
</div>
</body>
</html>
```